Meridale Vantage Alliance Web Design

I would like a web design for a conference. Registration, Form completion, Hotel, Speakers etc. See link for sample similar but not the same.
http://qrvlo.example/pldwk/index.php/contact-us
We would like the design to depict the colours of the logo which is attached. A banner of the website will be provided. We would like a transitioning space in the top and front page of the website for announcements and showcase of events. We would like custom prepared headers for each grouping, example, Sponsor, Venue, Discussion etc.

Hotel

Coded - Design and coding required

```html
<!DOCTYPE html>
<html lang="en">
<head>
<meta charset="utf-8">
<title>Meridale Vantage Alliance Conference 2015 — Contact Us</title>
<link href="https://fonts.googleapis.com/css2?family=Raleway:wght@400;500;600&family=Open+Sans:wght@400;600&display=swap" rel="stylesheet">
<style>
:root{
  --blue:#1177c4;
  --orange:#f5951f;
  --pink:#ef1593;
  --green:#8dc63f;
  --teal:#1aaba8;
  --ink:#222;
  --text:#555;
  --grey-bg:#efefef;
  --frame:#e2e2e2;
  --black:#000;
  --white:#fff;
}
*{box-sizing:border-box;margin:0;padding:0}
html,body{width:1043px;height:1200px;overflow:hidden;background:var(--white);font-family:"Raleway",sans-serif;color:var(--text)}
.page{position:relative;width:1043px;height:1200px}
.abs{position:absolute}
.grey-band{left:0;top:131px;width:1043px;height:733px;background:var(--grey-bg)}
.brand{left:158px;top:22px;width:250px}
.brand-name{font-size:19px;font-weight:600;color:var(--ink);line-height:1.05;display:flex;align-items:center;gap:8px}
.brand-name .dot{width:42px;height:42px;border-radius:50%;background:var(--ink);flex:none}
.brand-place{font-size:7px;color:var(--orange);font-weight:600;margin-top:6px;letter-spacing:.2px}
.badge{left:578px;top:20px;width:64px;height:64px;border-radius:50%;background:#d93a2b}
.thanks{left:652px;top:70px;width:232px;font-family:"Open Sans",sans-serif;font-size:8.5px;color:#888;line-height:1.25}
.nav{left:163px;top:107px;width:716px;height:31px;background:var(--black);display:flex;padding-left:7px}
.nav a{color:var(--white);text-decoration:none;font-family:"Open Sans",sans-serif;font-size:9.6px;line-height:31px;padding:0 12px}
.nav a.active{background:var(--blue);padding:0 14px}
.slider-frame{left:156px;top:131px;width:730px;height:298px;background:var(--white)}
.slide{left:163px;top:138px;width:716px;height:283px;background:linear-gradient(90deg,#cfd5da 0%,#e9ecef 35%,#3a3f4a 55%,#d9dde2 100%)}
.slider-shadow{left:180px;top:429px;width:690px;height:18px;background:radial-gradient(ellipse at top,rgba(0,0,0,.22),rgba(0,0,0,0) 70%)}
.arrow{top:378px;width:28px;height:28px}
.panel{left:149px;top:487px;width:505px;height:339px;background:var(--white);padding:20px 24px}
.panel h1{font-weight:400;font-size:23px;color:var(--ink);letter-spacing:-.2px}
.panel h2{font-weight:500;font-size:13px;color:var(--blue);margin-top:4px}
.panel p{font-size:10.2px;line-height:1.25;margin-top:25px}
.panel p.tight{margin-top:13px}
.panel a{color:var(--green);text-decoration:none}
.shares{display:flex;gap:6px;margin-top:36px}
.share{display:flex;align-items:center;font-family:"Open Sans",sans-serif;font-size:7.5px}
.share .btn{height:15px;line-height:15px;padding:0 5px;border:1px solid #bbb;border-radius:2px;background:#f4f4f4;color:#333;font-weight:600}
.share .btn.solid{background:#3b5998;border-color:#3b5998;color:var(--white)}
.share .count{height:15px;line-height:13px;padding:0 4px;margin-left:3px;border:1px solid #ccc;color:#555;background:var(--white)}
.side{left:670px;width:224px;background:var(--frame);padding:7px 8px}
.side .head{height:31px;color:var(--white);font-size:13.5px;display:flex;align-items:center;gap:10px;padding-left:12px}
.side .body{background:var(--white)}
.sponsor{top:487px;height:162px}
.sponsor .head{background:var(--green)}
.sponsor .body{height:115px;display:flex;align-items:center;justify-content:center}
.sponsor-name{font-size:17px;font-weight:500;color:var(--ink)}
.weather{top:664px;height:162px}
.weather .head{background:var(--teal)}
.weather .body{height:115px;position:relative}
.cloud{left:14px;top:28px;width:60px;height:30px;border-radius:15px;background:linear-gradient(#eee,#bbb)}
.temp{left:22px;top:75px;font-family:"Open Sans",sans-serif;font-size:12px;color:#333}
.city{left:80px;top:27px;font-family:"Open Sans",sans-serif;font-weight:600;font-size:16px;color:#333}
.wx{left:80px;font-family:"Open Sans",sans-serif;font-size:8px;color:#555}
.card{top:903px;width:225px;height:224px;background:var(--frame);padding:7px}
.card .inner{height:210px;color:var(--white);padding:20px 12px 0;text-align:center}
.card .icon{width:61px;height:61px;border-radius:50%;background:rgba(255,255,255,.15);margin:0 auto;display:flex;align-items:center;justify-content:center}
.card h3{font-weight:400;font-size:18px;margin-top:8px}
.card p{text-align:left;font-size:10.2px;line-height:1.2;margin-top:6px}
.venue .inner{background:var(--blue)}
.notes .inner{background:var(--orange)}
.secretariat .inner{background:var(--pink)}
.footer{left:0;top:1162px;width:1043px;height:38px;background:var(--black);color:var(--white);font-size:9.5px;text-align:center;line-height:38px}
</style>
</head>
<body>
<div class="page">
  <div class="abs grey-band"></div>

  <header>
    <div class="abs brand">
      <div class="brand-name"><span class="dot"></span><span>10th Meridale Vantage Alliance Conference 2015</span></div>
      <div class="brand-place">PROVIDENCIALES, TURKS AND CAICOS ISLANDS, BWI.</div>
    </div>
    <div class="abs badge" role="img" aria-label="Anniversary badge"></div>
    <div class="abs thanks">A Big Thank You!! to all participants and sponsors for making the 8th hosting of this conference a success.</div>
  </header>

  <div class="abs slider-frame"></div>
  <nav class="abs nav">
    <a class="active">HOME</a><a>CONFERENCE INFO</a><a>PROGRAMME</a><a>SPEAKERS</a><a>PRESENTATIONS</a><a>10TH MVA - DEBRIEFING NOTES</a><a>PHOTO GALLERY</a>
  </nav>
  <div class="abs slide" role="img" aria-label="Photo of business people meeting in a bright office lounge"></div>
  <svg class="abs arrow" style="left:171px" viewBox="0 0 28 28"><circle cx="14" cy="14" r="12" fill="rgba(255,255,255,.6)" stroke="#555" stroke-width="2"/><path d="M16 8l-6 6 6 6" fill="none" stroke="#555" stroke-width="2.5"/></svg>
  <svg class="abs arrow" style="left:841px" viewBox="0 0 28 28"><circle cx="14" cy="14" r="12" fill="rgba(255,255,255,.6)" stroke="#555" stroke-width="2"/><path d="M12 8l6 6-6 6" fill="none" stroke="#555" stroke-width="2.5"/></svg>
  <div class="abs slider-shadow"></div>

  <main class="abs panel">
    <h1>CONTACT US</h1>
    <h2>SECRETARIAT</h2>
    <p>Meridale Vantage Alliance<br>The Quays, 4th floor<br>18 Larkspur Drive, Port Avery 3<br>Jamaica, West Indies<br>Phone: 1-(555)-014-2201, Fax: 1-(555)-014-2202<br>Email: <a>events@qrvlo.example</a></p>
    <p>Members of the the Secretariat (Meridale Vantage Alliance Staff) and Board of Directors and will be onsite. In the event of an emergency please contact Delphine Arworth, Tel.: 555-014-2270.</p>
    <p class="tight">On the ground operational hours of the Secretariat during the conference will be from Monday November 11, 2013 to Friday November 15, 2013.</p>
    <div class="shares">
      <div class="share"><span class="btn">Share</span><span class="count">0</span></div>
      <div class="share"><span class="btn solid">Share</span><span class="count">0</span></div>
      <div class="share"><span class="btn">Post</span><span class="count">0</span></div>
      <div class="share"><span class="btn">+1</span><span class="count">0</span></div>
      <div class="share" style="margin-left:8px"><span class="btn solid">Like</span><span class="count">0</span></div>
    </div>
  </main>

  <aside class="abs side sponsor">
    <div class="head">
      <svg width="30" height="18" viewBox="0 0 30 18"><path d="M2 9l6-6 5 3 4-3 5 2 6 4-6 6-6-4-4 3-5-3z" fill="none" stroke="#fff" stroke-width="1.6"/></svg>
      SPONSORS
    </div>
    <div class="body"><div class="sponsor-name">Corvell Ashgrove</div></div>
  </aside>

  <aside class="abs side weather">
    <div class="head">
      <svg width="28" height="18" viewBox="0 0 28 18"><path d="M6 17a5 5 0 010-10 7 7 0 0113-1 5.5 5.5 0 013 11z" fill="#fff"/></svg>
      WEATHER
    </div>
    <div class="body">
      <div class="abs cloud" role="img" aria-label="Cloudy weather icon"></div>
      <div class="abs city">Montego Bay</div>
      <div class="abs wx" style="top:52px">Humidity: 74%</div>
      <div class="abs wx" style="top:68px">Wind: N at 2 mph</div>
      <div class="abs temp">79°F</div>
    </div>
  </aside>

  <section class="abs card venue" style="left:149px">
    <div class="inner">
      <div class="icon"><svg width="26" height="34" viewBox="0 0 26 34"><path d="M13 2a11 11 0 0111 11c0 8-11 19-11 19S2 21 2 13A11 11 0 0113 2z" fill="#fff"/><circle cx="13" cy="13" r="5" fill="#1177c4"/></svg></div>
      <h3>Venue</h3>
      <p>Et harum quidem rerum facilis est et expedita distinctio. Nam libero tempore, cum soluta nobis est eligendi optio cumque nihil impedit quo minus id quod maxime placeat facere.</p>
    </div>
  </section>
  <section class="abs card notes" style="left:409px">
    <div class="inner">
      <div class="icon"><svg width="26" height="30" viewBox="0 0 26 30"><rect x="3" y="2" width="18" height="24" fill="none" stroke="#fff" stroke-width="2"/><path d="M7 8h10M7 12h10M7 16h7" stroke="#fff" stroke-width="2"/></svg></div>
      <h3>10th MVA Notes</h3>
      <p>At vero eos et accusamus et iusto odio dignissimos ducimus qui blanditiis praesentium voluptatum deleniti atque corrupti quos dolores et quasmolestias excpturi sint occaecati.</p>
    </div>
  </section>
  <section class="abs card secretariat" style="left:669px">
    <div class="inner">
      <div class="icon"><svg width="32" height="22" viewBox="0 0 32 22"><rect x="1" y="1" width="30" height="20" fill="none" stroke="#fff" stroke-width="2"/><path d="M1 1l15 11L31 1" fill="none" stroke="#fff" stroke-width="2"/></svg></div>
      <h3>Secretariat</h3>
      <p>Et harum quidem rerum facilis est et expedita distinctio. Nam libero tempore, cum soluta nobis est eligendi optio cumque nihil impedit quo minus id quod maxime placeat facere.</p>
    </div>
  </section>

  <footer class="abs footer">10th Meridale Vantage Alliance Conference 2015</footer>
</div>
</body>
</html>
```